Tolvern Business Cards

Business card design. dont mind if new logo is suggested.
it would be for a security company.
our clients would be bigger security companies around Australia.
have a logo done but can be replaced. see attaached. like the colors.
Need company name, person name, designation, phone and email on front.
At back company logo and name. website saddress and 2 x license numbers
would like to have 2 different background color for both sidde

Industry/Entity Type

Security

Contact Information for Business Card

round corners, front should be light in color. need logo at back with webaddress and 2 x license numners

Font styles to use
Sans Serif

Colors
f37122
faa54b
f8ba93
0255a3
0592cd
85cae6
b3d448
9bcb3c
ffffff

Requirements
Must have
• see description
Nice to have
• see description
Should not have
• should not be difficult to read or hardd to find information on card.. lets say easy on eyes yet catchy

```html
<!DOCTYPE html>
<html lang="en">
<head>
<meta charset="utf-8">
<title>Tolvern Security Group – Business Cards</title>
<link rel="stylesheet" href="https://fonts.googleapis.com/css2?family=Open+Sans:wght@400;600&family=PT+Serif:wght@700&display=swap">
<style>
  :root {
    --stage: #a7c0e6;
    --slate: #8e8f8f;
    --charcoal: #283136;
    --navy: #1f3560;
    --blue: #0255a3;
    --sky: #85cae6;
    --orange: #f37122;
    --orange-light: #faa54b;
    --peach: #f8ba93;
    --white: #ffffff;
    --front-grey: #e3e6e9;
    --front-mint: #cfe6da;
    --ink: #2f3336;
    --muted: #55595c;
    --name-grey: #86898c;
  }
  html, body { margin: 0; padding: 0; width: 1200px; height: 927px; overflow: hidden; background: var(--stage); }
  .canvas { display: block; width: 1200px; height: 927px; }
  .brand-name { font-family: "PT Serif", Georgia, serif; font-weight: 700; }
  .detail { font-family: "Open Sans", Arial, sans-serif; font-weight: 400; }
  .contact { font-family: "Open Sans", Arial, sans-serif; font-weight: 400; font-size: 6.8px; fill: var(--ink); }
  .icon-disc { fill: var(--white); }
  .icon-glyph { fill: var(--muted); }
</style>
</head>
<body>
<svg class="canvas" viewBox="0 0 792 612" width="1200" height="927" xmlns="http://www.w3.org/2000/svg">
  <defs>
    <clipPath id="clip-back-slate"><rect x="48" y="91" width="315" height="179" rx="10"/></clipPath>
    <clipPath id="clip-back-white"><rect x="420" y="91" width="316" height="179" rx="10"/></clipPath>
    <clipPath id="clip-front-grey"><rect x="62" y="305" width="315" height="180" rx="10"/></clipPath>
    <clipPath id="clip-front-mint"><rect x="435" y="305" width="315" height="180" rx="10"/></clipPath>
    <radialGradient id="dots-grey" cx="0.6" cy="0.45" r="0.6">
      <stop offset="0" stop-color="#c9ced3" stop-opacity="0.9"/>
      <stop offset="1" stop-color="#e3e6e9" stop-opacity="0"/>
    </radialGradient>
    <radialGradient id="dots-mint" cx="0.6" cy="0.45" r="0.6">
      <stop offset="0" stop-color="#b4d4c6" stop-opacity="0.9"/>
      <stop offset="1" stop-color="#cfe6da" stop-opacity="0"/>
    </radialGradient>
  </defs>

  <!-- Back card, slate -->
  <g class="card card-back card-back--slate" clip-path="url(#clip-back-slate)">
    <rect x="48" y="91" width="315" height="179" fill="var(--slate)"/>
    <rect x="48" y="250" width="315" height="20" fill="var(--charcoal)"/>
    <rect x="42" y="135" width="18" height="95" rx="5" fill="var(--blue)"/>
    <rect x="351" y="135" width="18" height="95" rx="5" fill="var(--blue)"/>
    <circle cx="205" cy="152" r="18" fill="var(--white)"/>
    <text class="brand-name" x="205" y="189" font-size="10" fill="var(--white)" text-anchor="middle">TOLVERN SECURITY GROUP</text>
    <text class="detail" x="205" y="201" font-size="6.3" fill="var(--white)" text-anchor="middle">www.tolvernsecuritygroup.com</text>
    <text class="detail" x="205" y="212" font-size="6.3" fill="var(--white)" text-anchor="middle">license N1 - license N2</text>
  </g>

  <!-- Back card, white -->
  <g class="card card-back card-back--white" clip-path="url(#clip-back-white)">
    <rect x="420" y="91" width="316" height="179" fill="var(--white)"/>
    <rect x="420" y="250" width="316" height="20" fill="var(--orange-light)"/>
    <rect x="414" y="135" width="18" height="95" rx="5" fill="var(--orange)"/>
    <rect x="724" y="135" width="18" height="95" rx="5" fill="var(--orange)"/>
    <circle cx="578" cy="150" r="18" fill="var(--blue)"/>
    <text class="brand-name" x="580" y="189" font-size="10" fill="var(--navy)" text-anchor="middle">TOLVERN SECURITY GROUP</text>
    <text class="detail" x="580" y="199" font-size="6.3" fill="var(--muted)" text-anchor="middle">www.tolvernsecuritygroup.com</text>
    <text class="detail" x="580" y="210" font-size="6.3" fill="var(--muted)" text-anchor="middle">license N1 - license N2</text>
  </g>

  <!-- Front card, grey -->
  <g class="card card-front card-front--grey" clip-path="url(#clip-front-grey)">
    <rect x="62" y="305" width="315" height="180" fill="var(--front-grey)"/>
    <rect class="decor-dots" x="190" y="325" width="187" height="160" fill="url(#dots-grey)" role="img" aria-label="Soft scattered circle pattern"/>
    <rect x="62" y="313" width="178" height="4" fill="var(--sky)"/>
    <path d="M224 305 H377 V331 H252 Q241 331 236 320 Q231 305 224 305 Z" fill="var(--blue)"/>
    <path d="M62 458 H252 Q272 458 280 470 Q286 485 296 485 H62 Z" fill="var(--charcoal)"/>
    <g class="contact-list">
      <circle class="icon-disc" cx="90" cy="352" r="9"/>
      <circle class="icon-glyph" cx="90" cy="349.5" r="2.6"/>
      <path class="icon-glyph" d="M85.5 357 Q86 352.5 90 352.5 Q94 352.5 94.5 357 Z"/>
      <text class="contact" x="108" y="355">PERSONAL NAME</text>

      <circle class="icon-disc" cx="90" cy="380" r="9"/>
      <rect class="icon-glyph" x="85" y="377" width="10" height="7" rx="1"/>
      <rect x="88" y="375" width="4" height="2.5" fill="none" stroke="var(--muted)" stroke-width="1"/>
      <text class="contact" x="108" y="383">DESIGNATION</text>

      <circle class="icon-disc" cx="90" cy="405" r="9"/>
      <path class="icon-glyph" d="M84.5 402 L90 398 L95.5 402 V409 H84.5 Z"/>
      <path d="M84.5 402 L90 406 L95.5 402" fill="none" stroke="var(--white)" stroke-width="0.8"/>
      <text class="contact" x="108" y="408">TSG@TOLVERN.COM</text>

      <circle class="icon-disc" cx="90" cy="431" r="9"/>
      <rect x="87" y="425.5" width="6" height="11" rx="1" fill="none" stroke="var(--muted)" stroke-width="1.1"/>
      <text class="contact" x="108" y="434">+375550012345678900</text>
    </g>
    <g class="brand-name" font-size="15.5" fill="var(--name-grey)" text-anchor="end">
      <text x="365" y="390">TOLVERN</text>
      <text x="365" y="407">SECURITY</text>
      <text x="365" y="424">GROUP</text>
    </g>
  </g>

  <!-- Front card, mint -->
  <g class="card card-front card-front--mint" clip-path="url(#clip-front-mint)">
    <rect x="435" y="305" width="315" height="180" fill="var(--front-mint)"/>
    <rect class="decor-dots" x="563" y="325" width="187" height="160" fill="url(#dots-mint)" role="img" aria-label="Soft scattered circle pattern"/>
    <rect x="435" y="313" width="178" height="4" fill="var(--peach)"/>
    <path d="M597 305 H750 V331 H625 Q614 331 609 320 Q604 305 597 305 Z" fill="var(--orange)"/>
    <path d="M435 458 H625 Q645 458 653 470 Q659 485 669 485 H435 Z" fill="var(--orange)"/>
    <g class="contact-list">
      <circle class="icon-disc" cx="463" cy="351" r="9"/>
      <circle class="icon-glyph" cx="463" cy="348.5" r="2.6"/>
      <path class="icon-glyph" d="M458.5 356 Q459 351.5 463 351.5 Q467 351.5 467.5 356 Z"/>
      <text class="contact" x="481" y="354">PERSONAL NAME</text>

      <circle class="icon-disc" cx="463" cy="379" r="9"/>
      <rect class="icon-glyph" x="458" y="376" width="10" height="7" rx="1"/>
      <rect x="461" y="374" width="4" height="2.5" fill="none" stroke="var(--muted)" stroke-width="1"/>
      <text class="contact" x="481" y="382">DESIGNATION</text>

      <circle class="icon-disc" cx="463" cy="404" r="9"/>
      <path class="icon-glyph" d="M457.5 401 L463 397 L468.5 401 V408 H457.5 Z"/>
      <path d="M457.5 401 L463 405 L468.5 401" fill="none" stroke="var(--white)" stroke-width="0.8"/>
      <text class="contact" x="481" y="407">TSG@TOLVERN.COM</text>

      <circle class="icon-disc" cx="463" cy="430" r="9"/>
      <rect x="460" y="424.5" width="6" height="11" rx="1" fill="none" stroke="var(--muted)" stroke-width="1.1"/>
      <text class="contact" x="481" y="433">+375550012345678900</text>
    </g>
    <g class="brand-name" font-size="15.5" fill="var(--navy)" text-anchor="end">
      <text x="738" y="390">TOLVERN</text>
      <text x="738" y="407">SECURITY</text>
      <text x="738" y="424">GROUP</text>
    </g>
  </g>
</svg>
</body>
</html>
```